Independence Day Graphics for Sale

I want to create 10 social media graphics (new Pictora size 4:5 (1080 x 1350 pixels) focusing on our July 4th Sale Graphics, using any of the pics attached. Use the attached pics, NO RANDOM STOCK PHOTOGRAPHY. For the color scheme of the graphics, they should all be complementary to the product colors in the photos.
You can add any of the photos attached but none are required. You can do some of the graphics in all text. I mainly need BOLD text that says one of the headlines (10 total) SEE ATTACHED WORD DOCUMENT for the headlines to use.

Target Market(s)

women looking to lose weight

Requirements
Must have
• pics attached and text attached

```html
<!DOCTYPE html>
<html lang="en">
<head>
<meta charset="utf-8">
<title>Independence Day Sale Graphics</title>
<link rel="stylesheet" href="https://fonts.googleapis.com/css2?family=Oswald:wght@500;600;700&family=Dancing+Script:wght@500&display=swap">
<style>
  :root {
    --backdrop: #808080;
    --card: #ffffff;
    --ink: #2b2b2b;
    --red: #c1272d;
    --red-bright: #d9262b;
    --plum: #7a3560;
    --blue: #2e4a9e;
    --forest: #1f463b;
    --pink: #c8619b;
    --indigo: #3b2d70;
    --mint: #86c6ad;
    --head: "Oswald", "Arial Narrow", sans-serif;
    --script: "Dancing Script", cursive;
  }
  * { margin: 0; padding: 0; box-sizing: border-box; }
  html, body { width: 1200px; height: 3119px; overflow: hidden; }
  body { background: var(--backdrop); position: relative; font-family: var(--head); color: var(--ink); }

  .card {
    position: absolute; width: 461px; height: 576px;
    background: var(--card); overflow: hidden;
  }
  .col-a { left: 131px; } .col-b { left: 609px; }
  .row-1 { top: 75px; } .row-2 { top: 670px; } .row-3 { top: 1265px; }
  .row-4 { top: 1862px; } .row-5 { top: 2459px; }

  .arcs { position: absolute; inset: 0; width: 461px; height: 576px; pointer-events: none; }
  .arcs circle { fill: none; stroke: var(--accent); stroke-width: 1; opacity: .55; }

  .line { position: absolute; font-weight: 600; line-height: 1; white-space: nowrap; letter-spacing: -.5px; }
  .accent { color: var(--accent); }
  .dark { color: var(--ink); }
  .script { position: absolute; font-family: var(--script); font-weight: 500; line-height: 1; white-space: nowrap; color: var(--ink); }

  .offer { position: absolute; left: 95px; display: flex; align-items: stretch; color: var(--accent); }
  .offer-num { font-size: 192px; font-weight: 600; line-height: .8; letter-spacing: -6px; padding-top: 8px; }
  .offer-unit { display: flex; flex-direction: column; justify-content: space-between; margin-left: 6px; padding: 10px 0 0; }
  .offer-pct { font-size: 104px; font-weight: 500; line-height: .8; }
  .offer-off { font-size: 62px; font-weight: 600; line-height: .78; letter-spacing: 1px; }
  .spark { position: absolute; width: 44px; height: 44px; }
  .spark path { fill: var(--ink); }
  .spark-top { right: -40px; top: -6px; }
  .spark-low { left: -34px; bottom: -2px; transform: rotate(180deg); }
</style>
</head>
<body>

<svg width="0" height="0" style="position:absolute">
  <defs>
    <g id="arc-set">
      <circle cx="438" cy="22" r="48"/><circle cx="438" cy="22" r="66"/>
      <circle cx="438" cy="22" r="84"/><circle cx="438" cy="22" r="108"/>
      <circle cx="80" cy="580" r="52"/><circle cx="80" cy="580" r="70"/>
      <circle cx="80" cy="580" r="88"/><circle cx="80" cy="580" r="104"/>
    </g>
    <g id="spark-set">
      <path d="M18 24 L40 6 L30 30 Z"/>
      <path d="M4 18 L14 4 L12 20 Z"/>
      <path d="M22 40 L38 36 L24 34 Z"/>
    </g>
  </defs>
</svg>

<!-- 1 -->
<section class="card col-a row-1" style="--accent: var(--red)">
  <svg class="arcs" viewBox="0 0 461 576"><use href="#arc-set"/></svg>
  <p class="line accent" style="left:63px;top:109px;font-size:34px;">July 4th</p>
  <p class="line dark" style="left:63px;top:145px;font-size:68px;">MEGA SALE!</p>
  <div class="offer" style="top:237px">
    <span class="offer-num">25</span>
    <span class="offer-unit"><span class="offer-pct">%</span><span class="offer-off">OFF</span></span>
    <svg class="spark spark-top" viewBox="0 0 44 44"><use href="#spark-set"/></svg>
    <svg class="spark spark-low" viewBox="0 0 44 44"><use href="#spark-set"/></svg>
  </div>
  <p class="script" style="left:127px;top:397px;font-size:58px;">Everything</p>
</section>

<!-- 2 -->
<section class="card col-b row-1" style="--accent: var(--plum)">
  <svg class="arcs" viewBox="0 0 461 576"><use href="#arc-set"/></svg>
  <p class="line accent" style="left:73px;top:66px;font-size:64px;">BIGGEST</p>
  <p class="line accent" style="left:73px;top:134px;font-size:32px;">4th of July</p>
  <p class="line dark" style="left:73px;top:170px;font-size:76px;">SALE EVER!</p>
  <div class="offer" style="top:270px;left:103px">
    <span class="offer-num">25</span>
    <span class="offer-unit"><span class="offer-pct">%</span><span class="offer-off">OFF</span></span>
    <svg class="spark spark-top" viewBox="0 0 44 44"><use href="#spark-set"/></svg>
    <svg class="spark spark-low" viewBox="0 0 44 44"><use href="#spark-set"/></svg>
  </div>
  <p class="script" style="left:157px;top:425px;font-size:58px;">Sitewide</p>
</section>

<!-- 3 -->
<section class="card col-a row-2" style="--accent: var(--blue)">
  <svg class="arcs" viewBox="0 0 461 576"><use href="#arc-set"/></svg>
  <p class="line accent" style="left:73px;top:60px;font-size:62px;">HISTORIC</p>
  <p class="line accent" style="left:70px;top:126px;font-size:30px;">4th of July</p>
  <p class="line dark" style="left:70px;top:160px;font-size:86px;">Sale!</p>
  <div class="offer" style="top:275px;left:100px">
    <span class="offer-num">25</span>
    <span class="offer-unit"><span class="offer-pct">%</span><span class="offer-off">OFF</span></span>
    <svg class="spark spark-top" viewBox="0 0 44 44"><use href="#spark-set"/></svg>
    <svg class="spark spark-low" viewBox="0 0 44 44"><use href="#spark-set"/></svg>
  </div>
  <p class="script" style="left:148px;top:436px;font-size:54px;">of Everything</p>
</section>

<!-- 4 -->
<section class="card col-b row-2" style="--accent: var(--forest)">
  <svg class="arcs" viewBox="0 0 461 576"><use href="#arc-set"/></svg>
  <p class="line accent" style="left:69px;top:96px;font-size:46px;">Mega Summer</p>
  <p class="line dark" style="left:69px;top:154px;font-size:72px;">BLOWOUT!</p>
  <div class="offer" style="top:251px;left:99px">
    <span class="offer-num">25</span>
    <span class="offer-unit"><span class="offer-pct">%</span><span class="offer-off">OFF</span></span>
    <svg class="spark spark-top" viewBox="0 0 44 44"><use href="#spark-set"/></svg>
    <svg class="spark spark-low" viewBox="0 0 44 44"><use href="#spark-set"/></svg>
  </div>
  <p class="script" style="left:136px;top:410px;font-size:58px;">Everything</p>
</section>

<!-- 5 -->
<section class="card col-a row-3" style="--accent: var(--red-bright)">
  <svg class="arcs" viewBox="0 0 461 576"><use href="#arc-set"/></svg>
  <p class="line accent" style="left:63px;top:58px;font-size:46px;">One-Time</p>
  <p class="line dark" style="left:63px;top:108px;font-size:104px;">ONLY</p>
  <div class="offer" style="top:236px;left:90px">
    <span class="offer-num">25</span>
    <span class="offer-unit"><span class="offer-pct">%</span><span class="offer-off">OFF</span></span>
    <svg class="spark spark-top" viewBox="0 0 44 44"><use href="#spark-set"/></svg>
    <svg class="spark spark-low" viewBox="0 0 44 44"><use href="#spark-set"/></svg>
  </div>
  <p class="script" style="left:121px;top:401px;font-size:58px;">of Everything!</p>
</section>

<!-- 6 -->
<section class="card col-b row-3" style="--accent: var(--pink)">
  <svg class="arcs" viewBox="0 0 461 576"><use href="#arc-set"/></svg>
  <p class="line accent" style="left:63px;top:70px;font-size:36px;">25% OFF</p>
  <p class="line dark" style="left:63px;top:110px;font-size:72px;">Stock-Up</p>
  <p class="line dark" style="left:63px;top:185px;font-size:72px;">Event</p>
  <div class="offer" style="top:278px;left:96px">
    <span class="offer-num">25</span>
    <span class="offer-unit"><span class="offer-pct">%</span><span class="offer-off">OFF</span></span>
    <svg class="spark spark-top" viewBox="0 0 44 44"><use href="#spark-set"/></svg>
    <svg class="spark spark-low" viewBox="0 0 44 44"><use href="#spark-set"/></svg>
  </div>
  <p class="script" style="left:151px;top:446px;font-size:40px;">All Supplements</p>
</section>

<!-- 7 -->
<section class="card col-a row-4" style="--accent: var(--indigo)">
  <svg class="arcs" viewBox="0 0 461 576"><use href="#arc-set"/></svg>
  <p class="line accent" style="left:65px;top:78px;font-size:48px;">The Lowest</p>
  <p class="line accent" style="left:65px;top:134px;font-size:48px;">Prices We've Ever</p>
  <p class="line dark" style="left:65px;top:190px;font-size:90px;">Offered!</p>
  <div class="offer" style="top:311px;left:93px">
    <span class="offer-num">25</span>
    <span class="offer-unit"><span class="offer-pct">%</span><span class="offer-off">OFF</span></span>
    <svg class="spark spark-top" viewBox="0 0 44 44"><use href="#spark-set"/></svg>
    <svg class="spark spark-low" viewBox="0 0 44 44"><use href="#spark-set"/></svg>
  </div>
</section>

<!-- 8 -->
<section class="card col-b row-4" style="--accent: var(--mint)">
  <svg class="arcs" viewBox="0 0 461 576"><use href="#arc-set"/></svg>
  <p class="line accent" style="left:65px;top:48px;font-size:46px;">Our Biggest</p>
  <p class="line dark" style="left:65px;top:100px;font-size:74px;">DISCOUNT</p>
  <p class="line dark" style="left:65px;top:185px;font-size:74px;">EVER!</p>
  <div class="offer" style="top:278px;left:93px">
    <span class="offer-num">25</span>
    <span class="offer-unit"><span class="offer-pct">%</span><span class="offer-off">OFF</span></span>
    <svg class="spark spark-top" viewBox="0 0 44 44"><use href="#spark-set"/></svg>
    <svg class="spark spark-low" viewBox="0 0 44 44"><use href="#spark-set"/></svg>
  </div>
  <p class="script" style="left:132px;top:436px;font-size:58px;">Everything</p>
</section>

<!-- 9 -->
<section class="card col-a row-5" style="--accent: var(--red)">
  <svg class="arcs" viewBox="0 0 461 576"><use href="#arc-set"/></svg>
  <p class="line dark" style="left:63px;top:126px;font-size:74px;">Don’t Wait!</p>
  <div class="offer" style="top:226px;left:93px">
    <span class="offer-num">25</span>
    <span class="offer-unit"><span class="offer-pct">%</span><span class="offer-off">OFF</span></span>
    <svg class="spark spark-top" viewBox="0 0 44 44"><use href="#spark-set"/></svg>
    <svg class="spark spark-low" viewBox="0 0 44 44"><use href="#spark-set"/></svg>
  </div>
  <p class="script" style="left:117px;top:402px;font-size:58px;">Ends Soon</p>
</section>

<!-- 10 -->
<section class="card col-b row-5" style="--accent: var(--plum)">
  <svg class="arcs" viewBox="0 0 461 576"><use href="#arc-set"/></svg>
  <p class="line" style="left:63px;top:76px;font-size:60px;"><span class="accent">Last</span> <span class="dark">Chance</span></p>
  <div class="offer" style="top:166px;left:93px">
    <span class="offer-num">25</span>
    <span class="offer-unit"><span class="offer-pct">%</span><span class="offer-off">OFF</span></span>
    <svg class="spark spark-top" viewBox="0 0 44 44"><use href="#spark-set"/></svg>
    <svg class="spark spark-low" viewBox="0 0 44 44"><use href="#spark-set"/></svg>
  </div>
  <p class="line dark" style="left:63px;top:346px;font-size:58px;">Time Is</p>
  <p class="script accent" style="left:65px;top:406px;font-size:60px;color:var(--plum);">Running Out!</p>
</section>

</body>
</html>
```